依頼概要
■依頼の目的/概要
弊社が販売しているフルーツトマト(高糖度トマト)のパッケージのラベルデザインをお願いします。

■依頼詳細
弊社はトマトの栽培をしています。場所は長崎県壱岐市で玄界灘の島です。
ソラリム栽培というフィルムで栽培する新しい栽培方法です。島内のスーパーで販売しており大変好評です。糖度が8度以上あり、小さな子供さんからお年寄りまで喜んで食べて頂いています。トマト嫌いの人もこのトマトなら食べれるといって食べる方もいらっしゃいます。予想以上の好評で今回栽培面積を増やし関東への販路を考えております。これまで「ほしうらら」(子供が美味しくてパクパク食べてすぐ無くなり、また買ってと何回もせがまれママを泣かせる)というネーミングで販売していましたが。関東進出を期にネーミングを「紅澄野」又は「べに澄野」にバージョンアップして、新しいラベルの作成を企画しております。
<ラベルの仕様>
1.トマト1粒が20g~40gのミディートマトを150g~250gのパッケージで販売することを想定して、そのパッケージに貼るラベルです。
2.ラベルの大きさは、36×45角丸5R (mm)
3.ラベルに盛込む内容は添付ファイルの内容と同じで「ほしうらら」を「紅澄野」又は「べに澄野」に変更(デザインにマッチする方を選択して下さい)

■その他要望
高品質が売りですから、高級感と「一目で食べてみたい」と思うようなラベルにして欲しい。ネーミングは変更しない方がいいという方は「ほしうらら」のままでも構いません。
■ 選んだ理由

1.産地壱岐が強調されたデザインである。
2.表現したい項目が全て網羅されている。
3.デザインがシンプルでわかり易い。

■ 提案者全員のお礼・コメント

ラベルデザインの依頼は初めてでしたが、沢山のご提案を
頂き感謝しております。
多くの方のご提案有難うございました。

```html
<!DOCTYPE html>
<html lang="ja">
<head>
<meta charset="utf-8">
<title>紅澄野 ラベル案</title>
<link href="https://fonts.googleapis.com/css2?family=Noto+Sans+JP:wght@500;700&family=Noto+Serif+JP:wght@700&display=swap" rel="stylesheet">
<style>
  :root {
    --paper: #ffffff;
    --guide: #9a9a9a;
    --night: #0d0b0b;
    --forest: #1f4a34;
    --tomato: #c8101a;
    --tomato-deep: #6e0508;
    --tomato-light: #e5323a;
    --ink-light: #ffffff;
    --trim-line: #b8b8b8;
  }
  * { box-sizing: border-box; margin: 0; padding: 0; }
  html, body { width: 846px; height: 1200px; overflow: hidden; background: var(--paper); }
  body { position: relative; font-family: "Noto Sans JP", sans-serif; }

  .proof { position: absolute; }
  .proof--black-bleed { left: 107px; top: 228px; }
  .proof--black-trim  { left: 536px; top: 240px; }
  .proof--green-bleed { left: 107px; top: 672px; }
  .proof--green-trim  { left: 536px; top: 722px; }

  /* bleed proof with crop marks */
  .bleed { position: relative; width: 209px; height: 192px; overflow: visible; }
  .bleed .label { position: absolute; left: 16px; top: 16px; border-radius: 0; overflow: visible; }
  .bleed .label__bg { inset: -16px; border-radius: 0; }
  .bleed .trim-frame {
    position: absolute; left: 16px; top: 16px; width: 177px; height: 160px;
    border: 1px solid var(--trim-line); border-radius: 14px; pointer-events: none;
  }
  .crop-marks { position: absolute; left: -30px; top: -30px; width: 269px; height: 252px; overflow: visible; }
  .crop-marks line { stroke: var(--guide); stroke-width: 0.8; }

  /* label */
  .label {
    position: relative; width: 177px; height: 160px;
    border-radius: 14px; overflow: hidden; color: var(--ink-light); text-align: center;
  }
  .label__bg { position: absolute; inset: 0; border-radius: 14px; overflow: hidden; }
  .label--black .label__bg { background: var(--night); }
  .label--green .label__bg { background: var(--forest); }
  .label__tomato {
    position: absolute; left: 50%; top: 30%; width: 150%; height: 170%;
    transform: translateX(-50%); border-radius: 50%;
    background: radial-gradient(ellipse at 50% 30%, var(--tomato-light) 0%, var(--tomato) 35%, var(--tomato-deep) 80%);
  }
  .bleed .label__tomato { top: 36%; }

  .label__origin {
    position: absolute; left: 0; right: 0; top: 12px;
    font-size: 10.5px; font-weight: 500; letter-spacing: 0.02em; line-height: 1.2;
  }
  .label__name {
    position: absolute; left: 0; right: 0; top: 56px;
    font-family: "Noto Serif JP", serif; font-weight: 700; font-size: 31px; letter-spacing: 0.14em;
    line-height: 1;
  }
  .label__tagline {
    position: absolute; left: 0; right: 0; top: 93px;
    font-size: 6.5px; font-weight: 700; letter-spacing: 0.2em; line-height: 1.2;
  }
  .label__band { position: absolute; left: 0; right: 0; top: 104px; height: 6px; background: var(--ink-light); }
  .label__method {
    position: absolute; left: 0; right: 0; top: 116px;
    font-size: 8px; font-weight: 500; letter-spacing: 0.04em; line-height: 1.2;
  }
</style>
</head>
<body>

  <!-- black version, bleed proof -->
  <section class="proof proof--black-bleed">
    <div class="bleed">
      <svg class="crop-marks" viewBox="0 0 269 252">
        <line x1="0" y1="46" x2="36" y2="46"/><line x1="46" y1="0" x2="46" y2="36"/>
        <line x1="0" y1="30" x2="36" y2="30"/><line x1="30" y1="0" x2="30" y2="36"/>
        <line x1="233" y1="46" x2="269" y2="46"/><line x1="223" y1="0" x2="223" y2="36"/>
        <line x1="233" y1="30" x2="269" y2="30"/><line x1="239" y1="0" x2="239" y2="36"/>
        <line x1="0" y1="206" x2="36" y2="206"/><line x1="46" y1="216" x2="46" y2="252"/>
        <line x1="0" y1="222" x2="36" y2="222"/><line x1="30" y1="216" x2="30" y2="252"/>
        <line x1="233" y1="206" x2="269" y2="206"/><line x1="223" y1="216" x2="223" y2="252"/>
        <line x1="233" y1="222" x2="269" y2="222"/><line x1="239" y1="216" x2="239" y2="252"/>
        <line x1="94" y1="0" x2="175" y2="0"/><line x1="134.5" y1="0" x2="134.5" y2="20"/>
        <line x1="94" y1="252" x2="175" y2="252"/><line x1="134.5" y1="232" x2="134.5" y2="252"/>
        <line x1="0" y1="86" x2="0" y2="166"/><line x1="0" y1="126" x2="20" y2="126"/>
        <line x1="269" y1="86" x2="269" y2="166"/><line x1="249" y1="126" x2="269" y2="126"/>
      </svg>
      <div class="label label--black">
        <div class="label__bg"><div class="label__tomato" role="img" aria-label="真っ赤に熟したトマトの写真"></div></div>
        <p class="label__origin">長崎産フルーツトマト</p>
        <h2 class="label__name">紅澄野</h2>
        <p class="label__tagline">旨味 濃厚 高糖度</p>
        <div class="label__band"></div>
        <p class="label__method">ソラリム栽培トマト</p>
      </div>
      <div class="trim-frame"></div>
    </div>
  </section>

  <!-- black version, trimmed -->
  <section class="proof proof--black-trim">
    <div class="label label--black">
      <div class="label__bg"><div class="label__tomato" role="img" aria-label="真っ赤に熟したトマトの写真"></div></div>
      <p class="label__origin">長崎産フルーツトマト</p>
      <h2 class="label__name">紅澄野</h2>
      <p class="label__tagline">旨味 濃厚 高糖度</p>
      <div class="label__band"></div>
      <p class="label__method">ソラリム栽培トマト</p>
    </div>
  </section>

  <!-- green version, bleed proof -->
  <section class="proof proof--green-bleed">
    <div class="bleed">
      <svg class="crop-marks" viewBox="0 0 269 252">
        <line x1="0" y1="46" x2="36" y2="46"/><line x1="46" y1="0" x2="46" y2="36"/>
        <line x1="0" y1="30" x2="36" y2="30"/><line x1="30" y1="0" x2="30" y2="36"/>
        <line x1="233" y1="46" x2="269" y2="46"/><line x1="223" y1="0" x2="223" y2="36"/>
        <line x1="233" y1="30" x2="269" y2="30"/><line x1="239" y1="0" x2="239" y2="36"/>
        <line x1="0" y1="206" x2="36" y2="206"/><line x1="46" y1="216" x2="46" y2="252"/>
        <line x1="0" y1="222" x2="36" y2="222"/><line x1="30" y1="216" x2="30" y2="252"/>
        <line x1="233" y1="206" x2="269" y2="206"/><line x1="223" y1="216" x2="223" y2="252"/>
        <line x1="233" y1="222" x2="269" y2="222"/><line x1="239" y1="216" x2="239" y2="252"/>
        <line x1="94" y1="0" x2="175" y2="0"/><line x1="134.5" y1="0" x2="134.5" y2="20"/>
        <line x1="94" y1="252" x2="175" y2="252"/><line x1="134.5" y1="232" x2="134.5" y2="252"/>
        <line x1="0" y1="86" x2="0" y2="166"/><line x1="0" y1="126" x2="20" y2="126"/>
        <line x1="269" y1="86" x2="269" y2="166"/><line x1="249" y1="126" x2="269" y2="126"/>
      </svg>
      <div class="label label--green">
        <div class="label__bg"><div class="label__tomato" role="img" aria-label="真っ赤に熟したトマトの写真"></div></div>
        <p class="label__origin">長崎産フルーツトマト</p>
        <h2 class="label__name">紅澄野</h2>
        <p class="label__tagline">旨味 濃厚 高糖度</p>
        <div class="label__band"></div>
        <p class="label__method">ソラリム栽培トマト</p>
      </div>
      <div class="trim-frame"></div>
    </div>
  </section>

  <!-- green version, trimmed -->
  <section class="proof proof--green-trim">
    <div class="label label--green">
      <div class="label__bg"><div class="label__tomato" role="img" aria-label="真っ赤に熟したトマトの写真"></div></div>
      <p class="label__origin">長崎産フルーツトマト</p>
      <h2 class="label__name">紅澄野</h2>
      <p class="label__tagline">旨味 濃厚 高糖度</p>
      <div class="label__band"></div>
      <p class="label__method">ソラリム栽培トマト</p>
    </div>
  </section>

</body>
</html>
```